Clean Energy Brand - Business Card and Letterhead Designs

Hi, everyone! We need a graphic designer who has experience working with the energy sector. We want help designing a perfect two-sided business card and letterhead for a clean energy company we've been assisting. We have a great new logo and all of the associated files.Our client is looking for a design that is "disruptive," "future-facing," "masculine," "bold," and "empowering." The colours of the logo are navy blue and orange and are meant to stand out. We'll need all ownership and copyright paperwork as well as first proofs in a 48-hour period.

Target Market(s)

Government; Non-Profits; Clean Energy Industry; Municipalities; North American Energy Sector

Industry/Entity Type

Power Generation

Requirements
Must have
• A matching business card and letterhead design
Should not have
• Must not be from a template

```html
<!DOCTYPE html>
<html lang="en">
<head>
<meta charset="utf-8">
<title>Solmara – Stationery</title>
<link href="https://fonts.googleapis.com/css2?family=Roboto:wght@400;500&display=swap" rel="stylesheet">
<style>
  :root{
    --navy:#0f1f4d;
    --orange:#f05a14;
    --stage:#9a9a9a;
    --paper:#ffffff;
    --rule:#b9bcc2;
    --ink:#6b7585;
    --ink-dark:#2c2f36;
    --mark-faint:#f6f6f6;
  }
  *{box-sizing:border-box;margin:0;padding:0}
  html,body{width:1200px;height:971px;overflow:hidden}
  body{background:var(--stage);font-family:"Roboto",Arial,sans-serif;position:relative}

  .sheet,.card{position:absolute;background:var(--paper)}
  .accent-tab{position:absolute;background:linear-gradient(180deg,var(--orange),var(--navy))}

  .brand{display:flex;align-items:center;gap:6px;color:var(--navy);font-weight:500;letter-spacing:.01em;line-height:1}
  .brand-dot{border-radius:50%;background:var(--orange);flex:none}

  /* Letterhead */
  .letterhead{left:138px;top:86px;width:561px;height:775px}
  .letterhead .brand{position:absolute;left:0;right:0;top:48px;justify-content:center;font-size:26px}
  .letterhead .brand-dot{width:12px;height:12px}
  .letterhead .header-rule{position:absolute;left:0;right:0;top:105px;height:1px;background:var(--rule)}
  .letterhead .accent-tab{right:0;top:81px;width:16px;height:54px}
  .letterhead .backdrop-mark{position:absolute;left:55px;top:140px;width:440px;height:440px;border-radius:50%;background:var(--mark-faint)}
  .letterhead-footer{position:absolute;top:713px;left:0;right:0;font-size:9.5px;color:var(--ink);line-height:13px}
  .footer-item{position:absolute;display:flex;gap:8px}
  .footer-item .icons{display:flex;flex-direction:column;gap:2px;padding-top:1px}
  .footer-item svg{width:10px;height:11px}

  /* Business cards */
  .card-front{left:575px;top:377px;width:251px;height:157px}
  .card-back{left:834px;top:377px;width:251px;height:157px}
  .card-front .brand{position:absolute;left:14px;top:38px;font-size:17px}
  .card-front .brand-dot{width:8px;height:8px}
  .card-front .header-rule{position:absolute;left:0;right:10px;top:79px;height:1px;background:var(--rule)}
  .card-front .accent-tab{right:0;top:50px;width:10px;height:53px}
  .card-back .accent-tab{left:0;top:50px;width:9px;height:53px}
  .card-back .brand{position:absolute;left:0;right:0;top:78px;justify-content:center;font-size:18px}
  .card-back .brand-dot{width:8px;height:8px}

  .card-contacts{position:absolute;right:28px;top:87px;text-align:right;font-size:6.5px;color:var(--ink-dark);line-height:8.5px}
  .card-contacts .gap{height:5px}
  .card-contacts li{list-style:none;position:relative}
  .card-contacts svg{position:absolute;right:-13px;top:0;width:7px;height:8px}
  .card-web{position:absolute;left:0;right:0;top:117px;display:flex;justify-content:center;align-items:center;gap:4px;font-size:6.5px;color:var(--ink-dark)}
  .card-web svg{width:7px;height:7px}

  .icon{fill:none;stroke:var(--orange);stroke-width:1.2;stroke-linecap:round;stroke-linejoin:round}
</style>
</head>
<body>

<svg width="0" height="0" style="position:absolute">
  <defs>
    <symbol id="i-pin" viewBox="0 0 12 14"><path d="M6 13s-4.5-4.6-4.5-7.6a4.5 4.5 0 0 1 9 0C10.5 8.4 6 13 6 13z"/><circle cx="6" cy="5.5" r="1.6"/></symbol>
    <symbol id="i-phone" viewBox="0 0 12 12"><path d="M2 1.5l2 .2 1 2.5-1.3 1a7 7 0 0 0 3.1 3.1l1-1.3 2.5 1 .2 2c-5 .6-9-3.4-8.5-8.5z"/></symbol>
    <symbol id="i-mobile" viewBox="0 0 10 14"><rect x="1.5" y="1" width="7" height="12" rx="1.2"/><path d="M4 11h2"/></symbol>
    <symbol id="i-mail" viewBox="0 0 14 10"><rect x="1" y="1" width="12" height="8" rx=".5"/><path d="M1 1l6 4.5L13 1"/></symbol>
    <symbol id="i-globe" viewBox="0 0 12 12"><circle cx="6" cy="6" r="5"/><ellipse cx="6" cy="6" rx="2.2" ry="5"/><path d="M1 6h10"/></symbol>
  </defs>
</svg>

<section class="sheet letterhead">
  <div class="backdrop-mark" role="img" aria-label="Faint brand emblem backdrop"></div>
  <div class="brand"><span class="brand-dot"></span>solmara</div>
  <div class="header-rule"></div>
  <div class="accent-tab"></div>

  <footer class="letterhead-footer">
    <div class="footer-item" style="left:52px">
      <div class="icons"><svg class="icon" style="margin-top:6px"><use href="#i-pin"/></svg></div>
      <div>Your Address Line-1<br>Your Street 2000 View Location</div>
    </div>
    <div class="footer-item" style="left:240px">
      <div class="icons"><svg class="icon"><use href="#i-phone"/></svg><svg class="icon"><use href="#i-mobile"/></svg></div>
      <div>07 123456789<br>61 123456789</div>
    </div>
    <div class="footer-item" style="left:366px">
      <div class="icons"><svg class="icon"><use href="#i-mail"/></svg><svg class="icon"><use href="#i-globe"/></svg></div>
      <div>hello@solmara.com<br>www.solmara.com</div>
    </div>
  </footer>
</section>

<section class="card card-front">
  <div class="brand"><span class="brand-dot"></span>solmara</div>
  <div class="header-rule"></div>
  <div class="accent-tab"></div>
  <ul class="card-contacts">
    <li>Your Address Line<svg class="icon"><use href="#i-pin"/></svg></li>
    <li>Your Street 2000 View Location</li>
    <li class="gap"></li>
    <li>07 12345678<svg class="icon"><use href="#i-phone"/></svg></li>
    <li style="margin-top:2px">61 123456789<svg class="icon"><use href="#i-mobile"/></svg></li>
    <li>hello@solmara.com<svg class="icon"><use href="#i-mail"/></svg></li>
  </ul>
</section>

<section class="card card-back">
  <div class="accent-tab"></div>
  <div class="brand"><span class="brand-dot"></span>solmara</div>
  <div class="card-web"><svg class="icon"><use href="#i-globe"/></svg>www.solmara.com</div>
</section>

</body>
</html>
```